Flyer / Mailer for Business Debt Relief Business - Tillbrook Partners 6" x 11"

We need a 6" x 11" double sided flyer. This will be sent out to potential customers with high interest business loans. We would like the design to coordinate with the colors of our logo. I have included a mock up that we sketched out. I have also included a file of a mailer we received that we would like to use as a template (not colors or fonts, just set up). I have also included an .ai file of our logo.

```html
<!DOCTYPE html>
<html lang="en">
<head>
<meta charset="utf-8">
<title>Tillbrook Partners – Debt Relief Mailer</title>
<link rel="stylesheet" href="https://fonts.googleapis.com/css2?family=Montserrat:wght@400;600;700;800&family=Roboto:wght@500&display=swap">
<style>
  :root {
    --page: #000000;
    --blue: #0a7acb;
    --blue-deep: #0560a8;
    --green: #6cc04a;
    --green-bright: #7ed957;
    --header-bg: #f2f2f2;
    --footer-bg: #3f4042;
    --ink: #4a4a4a;
    --white: #ffffff;
    --rule: #bdbdbd;
  }
  * { margin: 0; padding: 0; box-sizing: border-box; }
  html, body { width: 1200px; height: 1200px; overflow: hidden; background: var(--page); }
  body { position: relative; font-family: "Montserrat", sans-serif; }

  .side { position: absolute; overflow: hidden; }

  /* FRONT */
  .front { left: 227px; top: 199px; width: 774px; height: 422px; background: var(--blue); }
  .photo { position: absolute; }
  .photo-column { position: absolute; left: 0; top: 0; width: 170px; height: 422px; }
  .photo-column .photo { left: 0; width: 170px; }
  .photo-meeting { top: 0; height: 86px; background: linear-gradient(135deg, #c9d3dc, #5d6b78 60%, #e8ecef); }
  .photo-seedling { top: 86px; height: 122px; background: radial-gradient(circle at 50% 50%, #7fa640, #b59c86 45%, #4d4a46); }
  .photo-charts { top: 208px; height: 114px; background: linear-gradient(160deg, #eef3f6, #b7cfe0 60%, #6aa7c9); }
  .photo-tech { top: 322px; height: 100px; background: linear-gradient(135deg, #1b2a44, #3e5f8a 55%, #0f1a2c); }

  .front-header { position: absolute; left: 170px; top: 0; width: 604px; height: 94px; background: var(--header-bg); }
  .headline { position: absolute; left: 24px; top: 34px; font-weight: 800; font-size: 21.5px; line-height: 20px; color: var(--blue); }
  .brand { position: absolute; display: flex; align-items: center; gap: 7px; color: #4b4b4b; font-weight: 400; letter-spacing: 1.5px; white-space: nowrap; }
  .brand .mark { width: 10px; height: 10px; background: var(--green); }
  .front .brand { right: 26px; top: 58px; font-size: 13px; }

  .photo-worker { top: 134px; left: 390px; width: 384px; height: 236px; background: linear-gradient(90deg, var(--blue) 0%, #4e8fb8 30%, #c9a27a 62%, #e8742a 80%, #5b6d80 100%); }

  .burden-band { position: absolute; left: 170px; top: 94px; width: 604px; height: 48px; background: var(--green); color: var(--white); font-weight: 700; font-size: 16px; line-height: 18px; padding: 5px 0 0 27px; clip-path: polygon(0 0, 100% 0, 100% 40px, 0 100%); }

  .offer { position: absolute; left: 194px; top: 161px; color: var(--white); }
  .offer-question { font-weight: 700; font-size: 13.5px; }
  .offer-answer { margin-top: 6px; font-weight: 800; font-size: 24px; color: var(--green-bright); }
  .benefits { list-style: none; margin-top: 0; font-family: "Roboto", sans-serif; font-weight: 500; font-size: 9.6px; }
  .benefits li { line-height: 15.7px; }
  .benefits li::before { content: "\2022"; color: var(--green-bright); margin-right: 3px; }

  .footer-rule { position: absolute; left: 170px; top: 370px; width: 604px; height: 4px; background: var(--green); }
  .front-footer { position: absolute; left: 170px; top: 374px; width: 604px; height: 48px; background: var(--footer-bg); color: var(--white); }
  .call { position: absolute; left: 19px; top: 11px; }
  .call-label { font-size: 7.5px; font-weight: 600; }
  .contact { display: flex; align-items: center; gap: 4px; margin-top: 3px; font-size: 13px; font-weight: 700; color: var(--green-bright); white-space: nowrap; }
  .contact .email { font-size: 12px; }
  .contact svg { flex: none; }
  .site { position: absolute; left: 374px; top: 12px; font-size: 11px; }
  .site strong { color: var(--green-bright); }
  .site .url { font-size: 13px; }

  /* BACK */
  .back { left: 231px; top: 642px; width: 767px; height: 418px; background: var(--white); }
  .back-bar { position: absolute; left: 0; top: 0; width: 375px; height: 6px; background: var(--green); }
  .return-address { position: absolute; left: 43px; top: 66px; font-size: 13.6px; line-height: 17.6px; color: var(--ink); font-style: normal; }
  .back .brand { left: 200px; top: 95px; font-size: 11px; letter-spacing: 1px; }
  .photo-desk { left: 0; top: 194px; width: 470px; height: 224px; background: linear-gradient(90deg, rgba(255,255,255,0) 60%, var(--white) 100%), linear-gradient(180deg, #f3f3f3, #e2e2e2 60%, #d4d4d4); }
  .tagline-band { position: absolute; left: 0; top: 127px; width: 375px; height: 67px; background: var(--blue); color: var(--white); font-weight: 800; font-size: 18.5px; line-height: 22px; padding: 14px 0 0 43px; }
  .pitch { position: absolute; left: 43px; top: 212px; width: 305px; font-size: 15px; line-height: 17.6px; color: var(--ink); }
  .pitch p + p { margin-top: 18px; }
  .stamp { position: absolute; left: 659px; top: 34px; width: 61px; height: 61px; border: 1px solid #c8c8c8; }
  .mail-line { position: absolute; left: 461px; width: 259px; height: 1px; background: var(--rule); }
</style>
</head>
<body>

<section class="side front">
  <div class="photo-column">
    <div class="photo photo-meeting" role="img" aria-label="Business team meeting around a table"></div>
    <div class="photo photo-seedling" role="img" aria-label="Hands holding coins with a green seedling"></div>
    <div class="photo photo-charts" role="img" aria-label="Financial charts and calculator on a desk"></div>
    <div class="photo photo-tech" role="img" aria-label="Hand touching a digital data display"></div>
  </div>

  <header class="front-header">
    <h1 class="headline">HELPING BUSINESS FOCUS ON<br>WHAT METTERS!</h1>
    <div class="brand"><span class="mark"></span>TILLBROOK PARTNERS</div>
  </header>

  <div class="photo photo-worker" role="img" aria-label="Construction worker in hard hat and safety vest on a building site"></div>

  <div class="burden-band">We understand that merchant cash advance loans can be a burden on your business.</div>

  <div class="offer">
    <p class="offer-question">OVER WHELMED BY DAILY/ WEEKLY PAYMENTS?</p>
    <p class="offer-answer">WE CAN HELP!</p>
    <ul class="benefits">
      <li>This is not a loan, WE ARE NOT LEADERS</li>
      <li>Improve your business cash flow immediately</li>
      <li>Move payments to one monthly amount</li>
      <li>Reduce the amount you are paying out monthly</li>
      <li>Strategic alternative to high interest loans</li>
      <li>Fast, confidential business debt relief</li>
      <li>No-obligation consultation</li>
      <li>Absolutely no credit pulls</li>
      <li>No collateral, no financials</li>
    </ul>
  </div>

  <div class="footer-rule"></div>
  <footer class="front-footer">
    <div class="call">
      <p class="call-label">CALL NOW FOR FREE CONSULTATION WITH OUR EXPERTS</p>
      <p class="contact">
        <svg width="11" height="11" viewBox="0 0 24 24"><path fill="#ffffff" d="M6.6 10.8a15.1 15.1 0 0 0 6.6 6.6l2.2-2.2c.3-.3.7-.4 1-.2 1.1.4 2.3.6 3.6.6.6 0 1 .4 1 1V20c0 .6-.4 1-1 1A17 17 0 0 1 3 4c0-.6.4-1 1-1h3.5c.6 0 1 .4 1 1 0 1.3.2 2.5.6 3.6.1.3 0 .7-.2 1z"/></svg>
        <span>800-555-0142</span>
        <svg width="11" height="11" viewBox="0 0 24 24"><circle cx="12" cy="12" r="11" fill="#ffffff"/><path d="M6 8h12v8H6z M6 8l6 5 6-5" fill="none" stroke="#3f4042" stroke-width="1.6"/></svg>
        <span class="email">info@tillbrookpartners.com</span>
      </p>
    </div>
    <div class="site">
      <p>VISIT OUT WEBSITE:</p>
      <p class="url">www.<strong>tillbrookpartners</strong>.com</p>
    </div>
  </footer>
</section>

<section class="side back">
  <div class="back-bar"></div>
  <address class="return-address">1450 Harlow Ave<br>Brenton | Marlow<br>County | 75012 USA</address>
  <div class="brand"><span class="mark"></span>TILLBROOK PARTNERS</div>

  <div class="photo photo-desk" role="img" aria-label="Faded desk scene with calculator, pen and piggy bank"></div>

  <h2 class="tagline-band">STRETEGIC DEBT RELIEF FOR<br>BUSINESS OF ALL SIZES</h2>

  <div class="pitch">
    <p>Stop taking out loans to pay off other loans.</p>
    <p>Take back your business's cash flow, and focus on what metters.</p>
  </div>

  <div class="stamp"></div>
  <div class="mail-line" style="top:205px"></div>
  <div class="mail-line" style="top:234px"></div>
  <div class="mail-line" style="top:264px"></div>
  <div class="mail-line" style="top:292px"></div>
</section>

</body>
</html>
```